Business Card Design Project

Colette Marvaux logo on front of card with 'of Sydney' added in small font.
Back of card needs to include the following information :

"Pure pleasure for the discerning gentleman" (I may omit once I've seen the design)

colettemarvaux.com.au

Contact by SMS or email only :

colette@colettemarvaux.com.au
Mobile : 0483 615 204 or + 61 483 615 204

Target Market(s)

Male professionals aged 20-60.

Industry/Entity Type

Business

Requirements
Must have
• Simple, bold, stylish and elegant.

```html
<!DOCTYPE html>
<html lang="en">
<head>
<meta charset="utf-8">
<title>Colette Marvaux of Sydney – Business Card</title>
<link href="https://fonts.googleapis.com/css2?family=Questrial&family=Playfair+Display:ital@1&display=swap" rel="stylesheet">
<style>
  :root {
    --stage: #3a3a3c;
    --card: #f4f3f5;
    --card-shade: #e2e0e4;
    --ink: #3b3440;
    --ink-soft: #5a5260;
    --plum: #b38ac2;
    --band: #4a4550;
    --band-light: #8d8892;
  }
  * { box-sizing: border-box; margin: 0; padding: 0; }
  html, body { width: 1200px; height: 900px; overflow: hidden; }
  body {
    background: var(--stage);
    font-family: "Questrial", "Century Gothic", sans-serif;
    color: var(--ink);
    position: relative;
  }
  .card {
    position: absolute;
    border-radius: 22px;
    background: linear-gradient(160deg, #ffffff 0%, var(--card) 55%, var(--card-shade) 100%);
    box-shadow: 0 14px 30px rgba(0,0,0,0.45);
    overflow: hidden;
  }
  .card--front { left: 110px; top: 70px; width: 580px; height: 330px; }
  .card--back  { left: 470px; top: 480px; width: 640px; height: 366px; }

  .wordmark { position: absolute; text-align: center; }
  .wordmark__name {
    display: block;
    font-size: 44px;
    letter-spacing: 1px;
    color: var(--ink);
    line-height: 1;
  }
  .wordmark__rule {
    display: block;
    height: 2px;
    margin: 10px auto 0;
    background: var(--ink-soft);
    width: 86%;
  }
  .wordmark__place {
    display: block;
    font-size: 15px;
    color: var(--ink-soft);
    margin-top: 12px;
  }
  .card--front .wordmark { left: 0; right: 0; top: 118px; }

  .card--back .wordmark { left: 36px; top: 46px; width: 300px; }
  .card--back .wordmark__name { font-size: 30px; }
  .card--back .wordmark__rule { margin-top: 8px; }
  .card--back .wordmark__place { font-size: 12px; margin-top: 8px; }

  .tagline {
    position: absolute;
    right: 0; top: 48px;
    width: 330px; height: 34px;
    border-radius: 17px 0 0 17px;
    background: linear-gradient(90deg, var(--band) 0%, var(--band-light) 55%, var(--band) 100%);
    font-family: "Playfair Display", serif;
    font-style: italic;
    font-size: 15px;
    color: var(--plum);
    display: flex; align-items: center;
    padding-left: 18px;
    white-space: nowrap;
  }

  .sweep { position: absolute; inset: 0; }

  .phone-block {
    position: absolute;
    left: 56px; top: 212px;
    display: flex; align-items: flex-start; gap: 16px;
  }
  .phone-block__numbers { text-align: center; font-size: 18px; line-height: 1.45; }
  .phone-block__or { font-size: 14px; }

  .contact-list { position: absolute; left: 356px; top: 212px; list-style: none; }
  .contact-list li {
    display: flex; align-items: center; gap: 16px;
    font-size: 15px; margin-bottom: 24px;
  }
  .icon { width: 20px; height: 20px; flex: none; }
</style>
</head>
<body>

<section class="card card--front" aria-label="Card front">
  <div class="wordmark">
    <span class="wordmark__name">Colette Marvaux</span>
    <span class="wordmark__rule" style="width:60%"></span>
    <span class="wordmark__place">of Sydney</span>
  </div>
</section>

<section class="card card--back" aria-label="Card back">
  <svg class="sweep" viewBox="0 0 640 366" aria-hidden="true">
    <path d="M150 366 C 300 250, 470 140, 640 100" fill="none" stroke="#4a4550" stroke-width="3"/>
    <path d="M158 366 C 306 256, 474 148, 640 110" fill="none" stroke="#c9c5cc" stroke-width="1.5"/>
  </svg>

  <div class="wordmark">
    <span class="wordmark__name">Colette Marvaux</span>
    <span class="wordmark__rule"></span>
    <span class="wordmark__place">of Sydney</span>
  </div>

  <div class="tagline">Pure pleasure for the discerning gentleman</div>

  <div class="phone-block">
    <svg class="icon" viewBox="0 0 20 20" aria-label="Mobile">
      <rect x="5" y="2" width="10" height="16" rx="2" fill="none" stroke="#3b3440" stroke-width="1.6"/>
      <line x1="8.5" y1="15" x2="11.5" y2="15" stroke="#3b3440" stroke-width="1.4"/>
    </svg>
    <div class="phone-block__numbers">
      <div>0483 615 204</div>
      <div class="phone-block__or">or</div>
      <div>+ 61 483 615 204</div>
    </div>
  </div>

  <ul class="contact-list">
    <li>
      <svg class="icon" viewBox="0 0 20 20" aria-label="Website">
        <path d="M2 10 L10 3 L18 10" fill="none" stroke="#3b3440" stroke-width="1.8"/>
        <path d="M5 9 V17 H15 V9" fill="none" stroke="#3b3440" stroke-width="1.8"/>
      </svg>
      <span>colettemarvaux.com.au</span>
    </li>
    <li>
      <svg class="icon" viewBox="0 0 20 20" aria-label="Email">
        <text x="10" y="15" text-anchor="middle" font-size="16" font-family="Questrial, sans-serif" fill="#3b3440">@</text>
      </svg>
      <span>colette@colettemarvaux.com.au</span>
    </li>
  </ul>
</section>

</body>
</html>
```